Popup Nightclub Grand Opening Flyer

We need to design a flyer for the grand opening of an upscale, exclusive nightclub called "Lanternfall". The design needs to be chic and exclusive. The background should be black and the text should primarily be white. We like minimalist designs.

Here is the text for the flyer
-
Velvetroom Atlanta Presents

Lanternfall (LOGO)

A Popup Nightclub Experience
For one night Only

Friday, October 18, 2013
Party begins at 9PM

INVITE ONLY

See invitation for location details
(Velvetroom Atlanta logo)

-
Examples we like

http://cdn2-b.plorvex-news.test/sites/default/files/styles/image_content_width/hash/3d/fb/4729105836_5521_flyer.jpg?itok=Q8rmZt2w

http://api.trevlomesh.test/files/9Kxq-Tr72PQd0hzXbwaLr8VMN2K617J3nqBw5CHR4XtdM8Y2sqEA-KjuxBnRoLW4QTyMHD8nwfYcJz-Rkh3vqp4MNaTYe9s1/7zenFridays.jpg

http://brenquist.test/wp-content/uploads/yootheme/widgetkit/gallery/7zen/7zen-gen_nvibe4-01.jpg
Updates

Hi All, one thing that we are seeing that we don't like is on over emphasis on the phrase "a popup nightclub experience" please don't make this the largest thing on the flyer

Target Market(s)

Target market is 25-35 year olds who are affluent (rich) and like luxury brands

Requirements
Must have
• Dark Background
Nice to have
• Velvetroom Logo on the bottom
Modern text that isn't curvy
Should not have
• Curved text

```html
<!DOCTYPE html>
<html lang="en">
<head>
<meta charset="utf-8">
<title>Lanternfall Nightclub – Velvetroom Atlanta Presents</title>
<link rel="stylesheet" href="https://fonts.googleapis.com/css2?family=Jost:wght@300;400&display=swap">
<style>
  :root {
    --ink-black: #000000;
    --ink-charcoal: #333333;
    --text-white: #ffffff;
    --text-soft: #d6d6d6;
    --text-muted: #555555;
    --divider: #5a5a5a;
    --mark-silver: #b4b4b4;
  }
  * { margin: 0; padding: 0; box-sizing: border-box; }
  html, body {
    width: 900px;
    height: 1200px;
    overflow: hidden;
    background: var(--ink-black);
  }
  .flyer {
    position: relative;
    width: 900px;
    height: 1200px;
    background: linear-gradient(to bottom, var(--ink-charcoal) 0%, #141414 22%, var(--ink-black) 40%, var(--ink-black) 100%);
    color: var(--text-white);
    font-family: "Jost", sans-serif;
    font-weight: 300;
    text-align: center;
  }
  .presenter {
    position: absolute;
    top: 180px;
    left: 0;
    width: 100%;
    display: flex;
    justify-content: center;
    align-items: center;
    gap: 14px;
  }
  .presenter-mark {
    width: 12px;
    height: 12px;
    border-radius: 50%;
    background: var(--text-white);
  }
  .presenter-name {
    font-size: 30px;
    letter-spacing: 2px;
    text-transform: uppercase;
    font-weight: 300;
  }
  .presents {
    position: absolute;
    top: 296px;
    left: 0;
    width: 100%;
    font-size: 16px;
    letter-spacing: 1.5px;
    color: var(--text-soft);
  }
  .venue-mark {
    position: absolute;
    top: 672px;
    left: 380px;
    width: 140px;
    height: 140px;
    border-radius: 50%;
    background: var(--mark-silver);
  }
  .venue {
    position: absolute;
    top: 860px;
    left: 0;
    width: 100%;
  }
  .venue-name {
    font-size: 50px;
    font-weight: 300;
    letter-spacing: 12px;
    text-transform: uppercase;
    line-height: 1;
    padding-left: 12px;
  }
  .venue-type {
    margin-top: 8px;
    font-size: 22px;
    font-weight: 400;
    letter-spacing: 4px;
    text-transform: uppercase;
    line-height: 1;
    padding-left: 4px;
  }
  .details {
    position: absolute;
    top: 1048px;
    left: 0;
    width: 100%;
    font-size: 20px;
    text-transform: uppercase;
    letter-spacing: 0.3px;
  }
  .details-row {
    display: flex;
    justify-content: center;
    align-items: center;
    line-height: 1;
  }
  .details-row + .details-row { margin-top: 20px; }
  .details-row .sep {
    color: var(--divider);
    margin: 0 22px;
  }
  .location-note {
    position: absolute;
    top: 1139px;
    left: 0;
    width: 100%;
    font-size: 11px;
    letter-spacing: 0.5px;
    color: var(--text-muted);
  }
</style>
</head>
<body>
  <main class="flyer">
    <header class="presenter">
      <span class="presenter-mark"></span>
      <span class="presenter-name">Velvetroom Atlanta</span>
    </header>
    <p class="presents">Presents</p>

    <span class="venue-mark"></span>
    <section class="venue">
      <h1 class="venue-name">Lanternfall</h1>
      <p class="venue-type">Nightclub</p>
    </section>

    <section class="details">
      <p class="details-row">
        <span>A Popup Nightclub Experience</span>
        <span class="sep">|</span>
        <span>For One Night Only</span>
      </p>
      <p class="details-row">
        <span>Friday, October 18, 2013</span>
        <span class="sep">|</span>
        <span>Party Begins at 9PM</span>
        <span class="sep">|</span>
        <span>Invite Only</span>
      </p>
    </section>

    <p class="location-note">See invitation for location details</p>
  </main>
</body>
</html>
```